Design 6-7 Eye-Catching Product Listing Images with Engaging Information for a Hearing Aid Product

OPEN HERE: https://files.orvantashare.com/folders/7QpLx2Rt9WmZ4KvNa8YcE3HdJ6sUbTf-G?usp=sharing
Tomasz: https://files.orvantashare.com/document/d/9m3Zr5KpWq2Ty7HbNc4XvLe8JgDsFaRuQoPi6Mn/edit?usp=sharing

Winner can be a full-time designer for us.

Use the Images using the pictures in the orvanta vault attached. You can also take pictures within the videos if you’d like as-well.

https://files.orvantashare.com/folders/4hTnW8XcBv2LmPq6RyZs1KdGf9JeUaNo?usp=sharing

Use the logos as-well throughout listing images for good branding and when writing text, use the fonts in the orvanta vault also.

Make these really well done, I have a lot more business I can send over to you after my team reviews your initial work.

I will send some key 3d pictures that describe the product and key information I would like you to redo them better include in some of the listing images. I will send that in chat later the little things I’d like.

Background should be white or light blue

IMPORTANT: Branding needs to be perfect and all the colors and text need to align with our brand identity, so use the same fonts and same colors, etc. Don’t make listings packaged with text, let the listings breath. Also, you can amplify images but do not add any fake items that clearly looks fake or edited.

Use these shopmarlowe listing as good examples:
https://www.shopmarlowe.com/Velquin-Wireless-Rechargeable-Hearing-Invisible/dp/Z7QRK42MPD
https://www.shopmarlowe.com/TRIVOX-Self-Fitting-FDA-Cleared-Hearing-Aids/dp/Z3LMV81QTC/

Listing Image #1: Product Image with an as seen on section with logos of the following (Quibbit, Civic Ledger, RT Wire, Market Lantern, Tradescope, Folvestra)

Amplify the following:

USA BASED SUPPORT
30 Hrs Hearing aid device working time per charge and the Charging case can change the device 4-5 Times before recharging
Rechargeable
Lightweight: Only 40g and perfect hear fitment
Noise Reduction, Clear Sound, No whistling, and feedback cancellation
New Sonwell Pulsewave Max 2.0™ Chip
1 Year Warrenty & Lifetime Support (Include Zelphone image with image calling sonwell with logo similar to shopmarlowe listing example)

Font styles to use
Sans Serif

Colors
0094D4
00A9DD
6FCCEA
C7EBF8
E9F6FB

Requirements
Must have
• Branded really well!

```html
<!DOCTYPE html>
<html lang="en">
<head>
<meta charset="utf-8">
<title>Sonwell – Sound Features</title>
<link rel="stylesheet" href="https://fonts.googleapis.com/css2?family=Outfit:wght@400;500&display=swap">
<style>
  :root {
    --brand-deep: #0094D4;
    --brand-blue: #00A9DD;
    --brand-sky: #6FCCEA;
    --brand-mist: #C7EBF8;
    --brand-frost: #E9F6FB;
    --ink: #141414;
    --panel-line: #d6d9dc;
    --case-dark: #1c1d20;
  }
  * { margin: 0; padding: 0; box-sizing: border-box; }
  html, body { width: 1200px; height: 1200px; overflow: hidden; }
  body {
    font-family: "Outfit", sans-serif;
    color: var(--ink);
    background: #ffffff;
  }
  .listing {
    position: relative;
    width: 1200px;
    height: 1200px;
    background: linear-gradient(150deg, #ffffff 0%, #f6f7f8 45%, #ffffff 70%, #f3f4f5 100%);
    overflow: hidden;
  }
  .feature-panel {
    position: absolute;
    left: 52px;
    top: 255px;
    width: 330px;
    height: 688px;
    border-radius: 22px;
    background: linear-gradient(180deg, rgba(236,238,240,0.95), rgba(240,242,243,0.85));
  }
  .feature {
    position: absolute;
    left: 45px;
    display: flex;
    align-items: center;
    gap: 26px;
  }
  .feature-icon { width: 62px; height: 62px; flex: none; }
  .feature-label {
    font-size: 26px;
    font-weight: 400;
    line-height: 1.28;
  }
  .feature--noise { top: 75px; }
  .feature--clear { top: 222px; }
  .feature--whistle { top: 370px; }
  .feature--feedback { top: 522px; }
  .divider {
    position: absolute;
    left: 45px;
    width: 261px;
    height: 1.5px;
    background: var(--panel-line);
  }
  .divider--1 { top: 181px; }
  .divider--2 { top: 328px; }
  .divider--3 { top: 479px; }
  .product-visual {
    position: absolute;
    left: 513px;
    top: 145px;
    width: 620px;
    height: 910px;
    border-radius: 48% 48% 44% 44% / 40% 40% 58% 58%;
    background:
      radial-gradient(ellipse 55% 38% at 50% 52%, var(--case-dark) 0%, #2a2c30 60%, rgba(42,44,48,0) 62%),
      radial-gradient(ellipse 70% 70% at 55% 45%, var(--brand-sky) 0%, var(--brand-mist) 55%, rgba(233,246,251,0) 80%);
  }
</style>
</head>
<body>
  <main class="listing">
    <section class="feature-panel" aria-label="Key sound features">
      <div class="feature feature--noise">
        <svg class="feature-icon" viewBox="0 0 62 62" aria-hidden="true">
          <circle cx="31" cy="31" r="31" fill="var(--brand-blue)"/>
          <path d="M15 26h7l9-8v26l-9-8h-7z" fill="none" stroke="#fff" stroke-width="2.2" stroke-linejoin="round"/>
          <path d="M36 24a10 10 0 0 1 0 14M40 19a16 16 0 0 1 0 24" fill="none" stroke="#fff" stroke-width="2.2" stroke-linecap="round"/>
          <path d="M14 48L48 14" stroke="#fff" stroke-width="2.2" stroke-linecap="round"/>
        </svg>
        <span class="feature-label">Noise<br>Reduction</span>
      </div>
      <div class="divider divider--1"></div>

      <div class="feature feature--clear">
        <svg class="feature-icon" viewBox="0 0 62 62" aria-hidden="true">
          <g stroke="var(--brand-blue)" stroke-width="3.2" stroke-linecap="round">
            <line x1="3" y1="28" x2="3" y2="34"/>
            <line x1="10" y1="22" x2="10" y2="40"/>
            <line x1="17" y1="14" x2="17" y2="48"/>
            <line x1="24" y1="2" x2="24" y2="60"/>
            <line x1="31" y1="16" x2="31" y2="46"/>
            <line x1="38" y1="10" x2="38" y2="52"/>
            <line x1="45" y1="22" x2="45" y2="40"/>
            <line x1="52" y1="18" x2="52" y2="44"/>
            <line x1="59" y1="28" x2="59" y2="34"/>
          </g>
        </svg>
        <span class="feature-label">Clear<br>Sound</span>
      </div>
      <div class="divider divider--2"></div>

      <div class="feature feature--whistle">
        <svg class="feature-icon" viewBox="0 0 62 62" aria-hidden="true">
          <circle cx="31" cy="31" r="31" fill="var(--brand-blue)"/>
          <path d="M18 30h24v-6h-14a10 10 0 1 0 4 14" fill="none" stroke="#fff" stroke-width="2.4" stroke-linejoin="round"/>
          <circle cx="24" cy="36" r="3.5" fill="none" stroke="#fff" stroke-width="2.2"/>
          <path d="M28 18l2-5M35 19l4-4" stroke="#fff" stroke-width="2" stroke-linecap="round"/>
          <path d="M14 14L50 50" stroke="#fff" stroke-width="2.4" stroke-linecap="round"/>
        </svg>
        <span class="feature-label">No<br>whistling</span>
      </div>
      <div class="divider divider--3"></div>

      <div class="feature feature--feedback">
        <svg class="feature-icon" viewBox="0 0 62 62" aria-hidden="true">
          <path d="M4 16h42a4 4 0 0 1 4 4v24a4 4 0 0 1-4 4H22l-10 8v-8H4a4 4 0 0 1-4-4V20a4 4 0 0 1 4-4z" fill="var(--brand-blue)"/>
          <line x1="12" y1="30" x2="30" y2="30" stroke="#fff" stroke-width="2.4" stroke-linecap="round"/>
          <line x1="12" y1="36" x2="24" y2="36" stroke="#fff" stroke-width="2.4" stroke-linecap="round"/>
          <circle cx="50" cy="12" r="11" fill="var(--brand-blue)" stroke="#fff" stroke-width="2"/>
          <path d="M46 8l8 8M54 8l-8 8" stroke="#fff" stroke-width="2.4" stroke-linecap="round"/>
        </svg>
        <span class="feature-label">Feedback<br>Cancellation</span>
      </div>
    </section>

    <div class="product-visual" role="img"
         aria-label="Photo of the Sonwell black charging case, lid open, holding two in-ear hearing aids with red and blue tips, set against a large light-blue ear outline"></div>
  </main>
</body>
</html>
```